New furniture company needs a cool, fresh Website - think lounjo.com, velmora.com

Quiltrest.com: We are launching a home (Shopify) furniture business, aimed at the young, discerning mid-market consumer. The aim is to compete with many furniture e-tailers, as well as more established retail brands.
We want the website to capture the hearts, minds and wallets of the target audience, placing Quiltrest.com firmly into the market place. Please look to Velmora.com for look and feel inspiration. We will be selling approx 15 products to start. I suggest using Shopify with the following theme please: – Hearth & Meadow – Cadenza – Ravel. Please see the logo below. The website needs to have a sophisticated feel for affordable aspirational furniture. Soft colours and homely text - please go with look and feel of Velmora.com. Please see a below file containing image of some sofas, chairs and footstools that will be for sale.
Many thanks

Target Market(s)

mid-market, young families looking for cool, affordable, easy to buy furniture

Industry/Entity Type

Furniture

Coding

Coded - Design and coding required

Number of Pages Required

5+ page

Font styles to use
Sans Serif

Colors
86cae7
cee9f5
3277b5
eaf2ce
fdf9ce
fff3d1
0255a3
e8e8e8
cbcbcb

Requirements
Must have
• Shopify
• http://www.velmora.com/hartwick-leather-large-sofa.html - great example of what we need it to look like
• logo as shown
• homepage
• products menu - sofas, seating, footstools, antique
• images of all products (examples provided) with ability to click on various fabric swatch samples and see the sofa in different fabrics and colours (check out lounjo.com)
• facility for social media
• facility to buy online
• "add to wishlist"
• "add to basket"
Nice to have
• I want it to have a light and airy feel, nothing too heavy or corporate. Needs to be very easily navigated and a simple approach
Should not have
• Dark, heavy colours

```html
<!DOCTYPE html>
<html lang="en">
<head>
<meta charset="utf-8">
<title>Quiltrest — Website Concept</title>
<link href="https://fonts.googleapis.com/css2?family=Roboto:wght@300;400;500;700&display=swap" rel="stylesheet">
<style>
  :root{
    --sky:#86cae7;
    --sky-pale:#cee9f5;
    --blue:#3277b5;
    --navy:#0255a3;
    --cream:#fdf9ce;
    --grey-light:#e8e8e8;
    --grey-mid:#cbcbcb;
    --form-bg:#f1f1f1;
    --ink:#2b2b2b;
    --muted:#7a7a7a;
    --canvas:#eef3f8;
    --white:#ffffff;
  }
  *{box-sizing:border-box;margin:0;padding:0}
  html,body{width:1200px;height:2740px;overflow:hidden}
  body{background:var(--canvas);font-family:'Roboto',Arial,sans-serif;color:var(--ink);position:relative}

  /* ---------- presentation heading ---------- */
  .intro{position:absolute;left:0;top:82px;width:1200px;text-align:center}
  .intro__brand{display:inline-flex;align-items:center;gap:12px;font-size:22px;font-weight:400;letter-spacing:6px;color:var(--navy)}
  .intro__mark{width:26px;height:26px;border-radius:50%;background:var(--blue)}
  .intro__title{margin-top:40px;font-size:24px;font-weight:700;color:var(--navy);letter-spacing:1px}
  .intro__text{margin-top:38px;font-size:13px;line-height:20px;color:var(--muted)}

  /* ---------- page shell (all sizes in em, page is 100em wide) ---------- */
  .page{position:absolute;background:var(--white);overflow:hidden;box-shadow:0 6px 24px rgba(20,50,90,.12)}
  .page--screen{left:363px;top:332px;width:472px;height:267px;font-size:4.72px}
  .page--home{left:296px;top:845px;width:489px;font-size:4.89px}
  .page--contact{left:296px;top:1904px;width:606px;font-size:6.06px}

  .topbar{height:4em;display:flex;justify-content:space-between;align-items:center;padding:0 5em;border-bottom:1px solid var(--grey-light)}
  .topbar__group{display:flex;gap:2.6em;align-items:center}
  .topbar__item{font-size:.85em;color:var(--muted);letter-spacing:.02em}

  .header{height:7em;display:flex;justify-content:space-between;align-items:center;padding:0 5em}
  .logo{display:flex;align-items:center;gap:.8em}
  .logo__mark{width:1.8em;height:1.8em;border-radius:50%;background:var(--sky)}
  .logo__name{font-size:1.3em;letter-spacing:.3em;color:var(--blue);font-weight:400}
  .nav{display:flex;align-items:center;gap:2.4em}
  .nav__link{font-size:.9em;color:var(--ink);font-weight:500;padding:1.2em 0}
  .nav__link--active{color:var(--blue);border-top:.25em solid var(--sky)}
  .nav__icon{width:1.8em;height:1.8em}

  .hero{position:relative;height:43em}
  .hero__photo{position:absolute;inset:0;background:linear-gradient(100deg,#e4e1dc 0%,#c9c2b8 30%,#8d7764 46%,#5e3f2c 60%,#4a3326 80%,#65564a 100%)}
  .hero__arrow{position:absolute;top:19em;width:2.4em;height:5em;background:rgba(60,60,60,.45)}
  .hero__arrow--prev{left:0}
  .hero__arrow--next{right:0}
  .hero__caption{position:absolute;left:59%;top:14em;color:var(--white)}
  .hero__kicker{font-size:1.5em;font-weight:500;letter-spacing:.05em}
  .hero__title{font-size:3.8em;font-weight:700;line-height:1.05;letter-spacing:.02em}
  .hero__sub{font-size:1em;letter-spacing:.06em}
  .hero__btn{display:inline-block;margin-top:1.8em;font-size:.9em;font-weight:700;color:var(--ink);background:var(--cream);padding:.9em 2em}
  .hero__dots{position:absolute;bottom:2em;left:0;right:0;display:flex;justify-content:center;gap:1em}
  .hero__dot{width:.8em;height:.8em;border-radius:50%;background:rgba(255,255,255,.6)}
  .hero__dot--on{background:var(--white)}

  .perks{height:23em;display:grid;grid-template-columns:repeat(3,1fr);padding:3.5em 10em}
  .perk{display:flex;flex-direction:column;align-items:center;justify-content:center;border-right:1px solid var(--grey-light)}
  .perk:last-child{border-right:0}
  .perk__icon{width:4.6em;height:4.6em;margin-bottom:1.2em}
  .perk__title{font-size:1.3em;font-weight:700}
  .perk__text{font-size:.85em;color:var(--muted);margin-top:.4em}

  .categories{height:28em;display:grid;grid-template-columns:repeat(4,1fr)}
  .category{display:flex;align-items:center;justify-content:center}
  .category__label{font-size:1.9em;color:var(--white);letter-spacing:.06em;font-weight:400}
  .category--sofas{background:linear-gradient(160deg,#c8c9ca,#e9e9e8 60%,#d4d4d3)}
  .category--seating{background:linear-gradient(160deg,#b9b8b6,#dedcd8 60%,#c7c3bd)}
  .category--footstools{background:linear-gradient(160deg,#a9a9a9,#d6d6d6 50%,#8a8a8a)}
  .category--antique{background:linear-gradient(160deg,#c2c2c2,#8c8c8c 60%,#6f6f6f)}

  .favourites{height:46em;padding-top:4em;text-align:center;position:relative}
  .favourites__title{font-size:2.3em;font-weight:500}
  .favourites__row{display:grid;grid-template-columns:repeat(4,1fr);gap:.8em;margin:4em 5em 0}
  .favourites__arrow{position:absolute;top:21em;width:1.6em;height:4em;background:var(--grey-mid)}
  .favourites__arrow--prev{left:3.4em}
  .favourites__arrow--next{right:3.4em}
  .product{text-align:left}
  .product__photo{height:23em;background:linear-gradient(180deg,#f2f2f2,#e3e3e3)}
  .product__photo--green{background:radial-gradient(circle at 50% 55%,#4d4a26 0 30%,#efefef 45%)}
  .product__photo--grey{background:linear-gradient(180deg,#5b5a58 0 40%,#b5b2ad 40% 70%,#e6e3de 70%)}
  .product__photo--tan{background:radial-gradient(circle at 50% 50%,#b59c82 0 28%,#f4f4f4 45%)}
  .product__photo--light{background:radial-gradient(circle at 50% 55%,#d3d3cf 0 32%,#f3f3f3 46%)}
  .product__name{font-size:.85em;font-weight:700;margin-top:1.3em}
  .product__stars{font-size:.75em;color:var(--sky)}
  .product__price{font-size:.8em;color:var(--muted)}

  .partners{height:13em;display:flex;justify-content:center;align-items:center;gap:5em;border-bottom:1px solid var(--grey-light)}
  .partner{width:6.5em;height:6.5em;border-radius:50%;border:.25em solid var(--grey-mid)}

  .newsletter{height:9em;background:var(--sky);display:flex;justify-content:space-between;align-items:center;padding:0 5em}
  .newsletter__title{font-size:1.6em;color:var(--white);font-weight:500;letter-spacing:.02em}
  .newsletter__form{display:flex}
  .newsletter__input{width:18em;height:3.2em;background:var(--white);font-size:1em;color:var(--muted);padding:.9em 1em}
  .newsletter__btn{height:3.2em;background:var(--navy);color:var(--white);font-size:1em;padding:1em 1.6em;font-weight:500}

  .footer{height:23em;display:grid;grid-template-columns:repeat(5,1fr);padding:4em 5em 0}
  .footer__heading{font-size:1em;font-weight:700;margin-bottom:1em}
  .footer__link{font-size:.85em;color:var(--muted);line-height:2.3;display:flex;align-items:center;gap:.6em}
  .footer__social{width:1.8em;height:1.8em;border-radius:50%;background:var(--blue)}

  .bottombar{height:5em;display:flex;justify-content:space-between;align-items:center;margin:0 5em;border-top:1px solid var(--grey-light)}
  .bottombar__copy{font-size:.8em;color:var(--muted)}
  .payments{display:flex;gap:.8em}
  .payment{width:3.4em;height:2.1em;border-radius:.3em;background:var(--grey-mid)}
  .payment--blue{background:var(--blue)}
  .payment--sky{background:var(--sky)}
  .payment--navy{background:var(--navy)}

  /* ---------- contact page ---------- */
  .contact{height:59em;background:var(--form-bg);padding-top:8em;text-align:center}
  .contact__title{font-size:2.4em;font-weight:700}
  .contact__lead{font-size:1em;color:var(--muted);line-height:1.6;margin-top:1.2em}
  .contact__form{width:44em;margin:2.4em auto 0;text-align:left}
  .contact__label{font-size:.9em;display:block;margin:1.2em 0 .6em}
  .contact__field{height:3.2em;background:var(--white);font-size:.85em;color:var(--muted);padding:1em}
  .contact__field--area{height:12em}
  .contact__submit{display:inline-block;margin-top:2em;background:var(--sky);color:var(--white);font-size:.85em;padding:1em 3em;font-weight:500}

  /* ---------- mobile page ---------- */
  .page--mobile{left:814px;top:845px;width:88px;height:995px}
  .m-top{height:10px;display:flex;justify-content:space-between;align-items:center;padding:0 4px;font-size:2.5px;color:var(--muted)}
  .m-header{height:22px;display:flex;justify-content:space-between;align-items:center;padding:0 4px}
  .m-logo{font-size:3.5px;letter-spacing:1px;color:var(--blue);display:flex;align-items:center;gap:2px}
  .m-logo__mark{width:5px;height:5px;border-radius:50%;background:var(--sky)}
  .m-burger{width:8px;height:6px;border-top:1px solid var(--ink);border-bottom:1px solid var(--ink);position:relative}
  .m-hero{height:136px;position:relative;background:linear-gradient(100deg,#e4e1dc 0%,#a8998a 35%,#5e3f2c 60%,#4a3326 100%)}
  .m-hero__caption{position:absolute;left:5px;top:52px;color:var(--white)}
  .m-hero__kicker{font-size:3px}
  .m-hero__title{font-size:6px;font-weight:700}
  .m-hero__btn{display:inline-block;margin-top:3px;background:var(--cream);color:var(--ink);font-size:2.5px;padding:1px 4px}
  .m-perk{height:54px;display:flex;flex-direction:column;align-items:center;justify-content:center;border-bottom:1px solid var(--grey-light)}
  .m-perk__icon{width:11px;height:11px;margin-bottom:3px}
  .m-perk__title{font-size:3px;font-weight:700}
  .m-perk__text{font-size:2.2px;color:var(--muted)}
  .m-category{height:98px;background:linear-gradient(160deg,#c8c9ca,#8a8a8a 60%,#b5b5b5);margin-top:4px}
  .m-section-title{font-size:3px;font-weight:700;text-align:center;margin:10px 0 6px}
  .m-product{margin:0 6px;height:64px;background:radial-gradient(circle at 50% 55%,#4d4a26 0 30%,#efefef 46%)}
  .m-product__meta{margin:3px 6px 0;font-size:2.4px;color:var(--muted)}
  .m-partners{display:flex;justify-content:center;gap:8px;margin:10px 0}
  .m-partners .partner{width:9px;height:9px;border-width:1px}
  .m-news{background:var(--sky);padding:8px 6px;text-align:center}
  .m-news__title{font-size:2.8px;color:var(--white);font-weight:500}
  .m-news__input{height:7px;background:var(--white);margin-top:4px}
  .m-news__btn{height:6px;background:var(--navy);margin-top:1px;color:var(--white);font-size:2.4px;line-height:6px}
  .m-footer{padding:8px 5px}
  .m-footer__heading{font-size:2.6px;font-weight:700;margin:5px 0 2px}
  .m-footer__link{font-size:2.3px;color:var(--muted);line-height:4.4px;display:flex;align-items:center;gap:2px}
  .m-footer__social{width:3.5px;height:3.5px;border-radius:50%;background:var(--blue)}
  .m-bottom{display:flex;justify-content:space-between;align-items:center;margin:2px 5px;border-top:1px solid var(--grey-light);padding-top:3px}
  .m-bottom__copy{font-size:2px;color:var(--muted)}
  .m-bottom .payment{width:5px;height:3px;border-radius:.5px}
  .m-bottom .payments{gap:1px}
</style>
</head>
<body>

<header class="intro">
  <div class="intro__brand"><span class="intro__mark"></span>QUILTREST</div>
  <h1 class="intro__title">WEBSITE</h1>
  <p class="intro__text">This is a concept website template for Quiltrest, with modern and unique design,<br>I tried to make something creative and unique for this theme</p>
</header>

<!-- desktop hero view -->
<section class="page page--screen">
  <div class="topbar">
    <div class="topbar__group"><span class="topbar__item">English ▾</span><span class="topbar__item">USD ▾</span></div>
    <div class="topbar__group"><span class="topbar__item">SITEMAP</span><span class="topbar__item">MY WISHLIST</span><span class="topbar__item">MY ACCOUNT</span><span class="topbar__item">MY CART</span><span class="topbar__item">SIGN IN</span></div>
  </div>
  <div class="header">
    <div class="logo"><span class="logo__mark"></span><span class="logo__name">QUILTREST</span></div>
    <nav class="nav">
      <span class="nav__link nav__link--active">HOME</span><span class="nav__link">CATEGORIES</span><span class="nav__link">PRODUCTS</span><span class="nav__link">FEATURES</span><span class="nav__link">BLOG</span><span class="nav__link">ABOUT US</span>
      <svg class="nav__icon" viewBox="0 0 20 20"><circle cx="8" cy="8" r="5.5" fill="none" stroke="#2b2b2b" stroke-width="1.6"/><line x1="12" y1="12" x2="17" y2="17" stroke="#2b2b2b" stroke-width="1.6"/></svg>
      <svg class="nav__icon" viewBox="0 0 20 20"><path d="M3 5h14l-2 9H5z" fill="none" stroke="#2b2b2b" stroke-width="1.5"/><circle cx="16" cy="4" r="3" fill="#3277b5"/></svg>
    </nav>
  </div>
  <div class="hero">
    <div class="hero__photo" role="img" aria-label="Living room with a large grey corner sofa, cushions, wood panel wall and a striped rug"></div>
    <span class="hero__arrow hero__arrow--prev"></span><span class="hero__arrow hero__arrow--next"></span>
    <div class="hero__caption">
      <div class="hero__kicker">EXTRA 20% OFF</div>
      <div class="hero__title">SOFFA COLLECTION</div>
      <div class="hero__sub">THE BEST SOFA COLLECTION STORE</div>
      <span class="hero__btn">LEARN MORE</span>
    </div>
    <div class="hero__dots"><span class="hero__dot hero__dot--on"></span><span class="hero__dot"></span><span class="hero__dot"></span></div>
  </div>
</section>

<!-- desktop homepage -->
<section class="page page--home">
  <div class="topbar">
    <div class="topbar__group"><span class="topbar__item">English ▾</span><span class="topbar__item">USD ▾</span></div>
    <div class="topbar__group"><span class="topbar__item">SITEMAP</span><span class="topbar__item">MY WISHLIST</span><span class="topbar__item">MY ACCOUNT</span><span class="topbar__item">MY CART</span><span class="topbar__item">SIGN IN</span></div>
  </div>
  <div class="header">
    <div class="logo"><span class="logo__mark"></span><span class="logo__name">QUILTREST</span></div>
    <nav class="nav">
      <span class="nav__link nav__link--active">HOME</span><span class="nav__link">CATEGORIES</span><span class="nav__link">PRODUCTS</span><span class="nav__link">FEATURES</span><span class="nav__link">BLOG</span><span class="nav__link">ABOUT US</span>
      <svg class="nav__icon" viewBox="0 0 20 20"><circle cx="8" cy="8" r="5.5" fill="none" stroke="#2b2b2b" stroke-width="1.6"/><line x1="12" y1="12" x2="17" y2="17" stroke="#2b2b2b" stroke-width="1.6"/></svg>
      <svg class="nav__icon" viewBox="0 0 20 20"><path d="M3 5h14l-2 9H5z" fill="none" stroke="#2b2b2b" stroke-width="1.5"/><circle cx="16" cy="4" r="3" fill="#3277b5"/></svg>
    </nav>
  </div>
  <div class="hero">
    <div class="hero__photo" role="img" aria-label="Living room with a large grey corner sofa, cushions, wood panel wall and a striped rug"></div>
    <span class="hero__arrow hero__arrow--prev"></span><span class="hero__arrow hero__arrow--next"></span>
    <div class="hero__caption">
      <div class="hero__kicker">EXTRA 20% OFF</div>
      <div class="hero__title">SOFFA COLLECTION</div>
      <div class="hero__sub">THE BEST SOFA COLLECTION STORE</div>
      <span class="hero__btn">LEARN MORE</span>
    </div>
    <div class="hero__dots"><span class="hero__dot hero__dot--on"></span><span class="hero__dot"></span><span class="hero__dot"></span></div>
  </div>

  <div class="perks">
    <div class="perk">
      <svg class="perk__icon" viewBox="0 0 24 24"><rect x="3" y="9" width="18" height="12" fill="#3277b5"/><rect x="2" y="6" width="20" height="4" fill="#86cae7"/><rect x="11" y="6" width="2" height="15" fill="#fff"/></svg>
      <div class="perk__title">REDEEM GIFT CART</div><div class="perk__text">Receive a gift on every sale</div>
    </div>
    <div class="perk">
      <svg class="perk__icon" viewBox="0 0 24 24"><rect x="1" y="6" width="14" height="10" fill="#86cae7"/><path d="M15 9h4l3 4v3h-7z" fill="#3277b5"/><circle cx="6" cy="18" r="2" fill="#3277b5"/><circle cx="18" cy="18" r="2" fill="#3277b5"/></svg>
      <div class="perk__title">FAST FREE SHIPMENT</div><div class="perk__text">For standard order over $150</div>
    </div>
    <div class="perk">
      <svg class="perk__icon" viewBox="0 0 24 24"><circle cx="12" cy="12" r="5" fill="#f2d98a"/><g stroke="#f2d98a" stroke-width="1.6"><line x1="12" y1="2" x2="12" y2="5"/><line x1="12" y1="19" x2="12" y2="22"/><line x1="2" y1="12" x2="5" y2="12"/><line x1="19" y1="12" x2="22" y2="12"/><line x1="5" y1="5" x2="7" y2="7"/><line x1="17" y1="17" x2="19" y2="19"/><line x1="5" y1="19" x2="7" y2="17"/><line x1="17" y1="7" x2="19" y2="5"/></g></svg>
      <div class="perk__title">24/7 SUPPORT</div><div class="perk__text">Feel free to contact us</div>
    </div>
  </div>

  <div class="categories">
    <div class="category category--sofas" role="img" aria-label="White lounge chair in a bright room"><span class="category__label">SOFAS</span></div>
    <div class="category category--seating" role="img" aria-label="White dining table with chairs"><span class="category__label">SEATING</span></div>
    <div class="category category--footstools" role="img" aria-label="Tall black bar stool"><span class="category__label">FOOTSTOOLS</span></div>
    <div class="category category--antique" role="img" aria-label="Dark classic armchair by a window"><span class="category__label">ANTIQUE</span></div>
  </div>

  <div class="favourites">
    <h2 class="favourites__title">OUR CUSTOMERS LOVE</h2>
    <span class="favourites__arrow favourites__arrow--prev"></span><span class="favourites__arrow favourites__arrow--next"></span>
    <div class="favourites__row">
      <div class="product"><div class="product__photo product__photo--light" role="img" aria-label="Light grey two-seat sofa"></div><div class="product__name">HARLOW RANGE</div><div class="product__stars">★★★★★</div><div class="product__price">£20.00</div></div>
      <div class="product"><div class="product__photo product__photo--green" role="img" aria-label="Olive green velvet sofa"></div><div class="product__name">MOSSBY RANGE</div><div class="product__stars">★★★★★</div><div class="product__price">£20.00</div></div>
      <div class="product"><div class="product__photo product__photo--grey" role="img" aria-label="Grey sofa beneath framed wall art"></div><div class="product__name">THE CARAWAY</div><div class="product__stars">★★★★★</div><div class="product__price">£20.00</div></div>
      <div class="product"><div class="product__photo product__photo--tan" role="img" aria-label="Tan upholstered armchair"></div><div class="product__name">WINFIELD BACK</div><div class="product__stars">★★★★★</div><div class="product__price">£20.00</div></div>
    </div>
  </div>

  <div class="partners"><span class="partner"></span><span class="partner"></span><span class="partner"></span><span class="partner"></span><span class="partner"></span><span class="partner"></span></div>

  <div class="newsletter">
    <div class="newsletter__title">SUBSCRIBE TO OUR NEWSLETTER</div>
    <div class="newsletter__form"><div class="newsletter__input">Enter your email address</div><div class="newsletter__btn">SUBSCRIBE</div></div>
  </div>

  <div class="footer">
    <div><div class="footer__heading">MY ACCOUNT</div><div class="footer__link">My Orders</div><div class="footer__link">My Vouchers</div><div class="footer__link">My Address</div><div class="footer__link">My Credit Slip</div><div class="footer__link">My History</div></div>
    <div><div class="footer__heading">INFORMATION</div><div class="footer__link">Contact Us</div><div class="footer__link">Search Terms</div><div class="footer__link">Shipping Guide</div><div class="footer__link">Term Of Use</div><div class="footer__link">Affiliate</div></div>
    <div><div class="footer__heading">EXTRA</div><div class="footer__link">Brand Partners</div><div class="footer__link">Gift Vouchers</div><div class="footer__link">Specials</div><div class="footer__link">Promotions</div><div class="footer__link">Wishlist</div></div>
    <div><div class="footer__heading">COLLECTION</div><div class="footer__link">Decorations</div><div class="footer__link">Living Room</div><div class="footer__link">Specials</div><div class="footer__link">Office Care</div><div class="footer__link">Kitchen Care</div></div>
    <div><div class="footer__heading">FOLLOW US</div><div class="footer__link"><span class="footer__social"></span>Facefolio</div><div class="footer__link"><span class="footer__social"></span>Chirper</div><div class="footer__link"><span class="footer__social"></span>Searchly+</div><div class="footer__link"><span class="footer__social"></span>Linkward</div></div>
  </div>
  <div class="bottombar">
    <span class="bottombar__copy">2017 © Copyright . All rights reserved</span>
    <div class="payments"><span class="payment payment--sky"></span><span class="payment payment--navy"></span><span class="payment"></span><span class="payment"></span><span class="payment payment--blue"></span><span class="payment payment--sky"></span></div>
  </div>
</section>

<!-- mobile homepage -->
<section class="page page--mobile">
  <div class="m-top"><span>English ▾ USD ▾</span><span>♡ ⌂</span></div>
  <div class="m-header"><div class="m-logo"><span class="m-logo__mark"></span>QUILTREST</div><span class="m-burger"></span></div>
  <div class="m-hero" role="img" aria-label="Living room with a large grey corner sofa">
    <div class="m-hero__caption"><div class="m-hero__kicker">EXTRA 20% OFF</div><div class="m-hero__title">SOFFA COLLECTION</div><span class="m-hero__btn">LEARN MORE</span></div>
  </div>
  <div class="m-perk"><svg class="m-perk__icon" viewBox="0 0 24 24"><rect x="3" y="9" width="18" height="12" fill="#3277b5"/><rect x="2" y="6" width="20" height="4" fill="#86cae7"/><rect x="11" y="6" width="2" height="15" fill="#fff"/></svg><div class="m-perk__title">REDEEM GIFT CART</div><div class="m-perk__text">Receive a gift on every sale</div></div>
  <div class="m-perk"><svg class="m-perk__icon" viewBox="0 0 24 24"><rect x="1" y="6" width="14" height="10" fill="#86cae7"/><path d="M15 9h4l3 4v3h-7z" fill="#3277b5"/><circle cx="6" cy="18" r="2" fill="#3277b5"/><circle cx="18" cy="18" r="2" fill="#3277b5"/></svg><div class="m-perk__title">FAST FREE SHIPMENT</div><div class="m-perk__text">For standard order over $150</div></div>
  <div class="m-perk"><svg class="m-perk__icon" viewBox="0 0 24 24"><circle cx="12" cy="12" r="6" fill="#f2d98a"/></svg><div class="m-perk__title">24/7 SUPPORT</div><div class="m-perk__text">Feel free to contact us</div></div>
  <div class="m-category" role="img" aria-label="Dark classic armchair by a window"></div>
  <div class="m-section-title">OUR CUSTOMERS LOVE</div>
  <div class="m-product" role="img" aria-label="Olive green velvet sofa"></div>
  <div class="m-product__meta">MOSSBY RANGE<br>£20.00</div>
  <div class="m-partners"><span class="partner"></span><span class="partner"></span><span class="partner"></span></div>
  <div class="m-news"><div class="m-news__title">SUBSCRIBE TO<br>OUR NEWSLETTER</div><div class="m-news__input"></div><div class="m-news__btn">SUBSCRIBE</div></div>
  <div class="m-footer">
    <div class="m-footer__heading">MY ACCOUNT</div><div class="m-footer__link">My Orders</div><div class="m-footer__link">My Vouchers</div><div class="m-footer__link">My Address</div><div class="m-footer__link">My Credit Slip</div><div class="m-footer__link">My History</div>
    <div class="m-footer__heading">INFORMATION</div><div class="m-footer__link">Contact Us</div><div class="m-footer__link">Search Terms</div><div class="m-footer__link">Shipping Guide</div><div class="m-footer__link">Term Of Use</div><div class="m-footer__link">Affiliate</div>
    <div class="m-footer__heading">EXTRA</div><div class="m-footer__link">Brand Partners</div><div class="m-footer__link">Gift Vouchers</div><div class="m-footer__link">Specials</div><div class="m-footer__link">Promotions</div><div class="m-footer__link">Wishlist</div>
    <div class="m-footer__heading">COLLECTION</div><div class="m-footer__link">Decorations</div><div class="m-footer__link">Living Room</div><div class="m-footer__link">Specials</div><div class="m-footer__link">Office Care</div><div class="m-footer__link">Kitchen Care</div>
    <div class="m-footer__heading">FOLLOW US</div><div class="m-footer__link"><span class="m-footer__social"></span>Facefolio</div><div class="m-footer__link"><span class="m-footer__social"></span>Chirper</div><div class="m-footer__link"><span class="m-footer__social"></span>Searchly+</div><div class="m-footer__link"><span class="m-footer__social"></span>Linkward</div>
  </div>
  <div class="m-bottom"><span class="m-bottom__copy">2017 © Copyright</span><div class="payments"><span class="payment payment--sky"></span><span class="payment payment--navy"></span><span class="payment"></span><span class="payment payment--blue"></span></div></div>
</section>

<!-- contact page -->
<section class="page page--contact">
  <div class="topbar">
    <div class="topbar__group"><span class="topbar__item">English ▾</span><span class="topbar__item">USD ▾</span></div>
    <div class="topbar__group"><span class="topbar__item">SITEMAP</span><span class="topbar__item">MY WISHLIST</span><span class="topbar__item">MY ACCOUNT</span><span class="topbar__item">MY CART</span><span class="topbar__item">SIGN IN</span></div>
  </div>
  <div class="header">
    <div class="logo"><span class="logo__mark"></span><span class="logo__name">QUILTREST</span></div>
    <nav class="nav">
      <span class="nav__link">HOME</span><span class="nav__link">CATEGORIES</span><span class="nav__link">PRODUCTS</span><span class="nav__link">FEATURES</span><span class="nav__link">BLOG</span><span class="nav__link">ABOUT US</span>
      <svg class="nav__icon" viewBox="0 0 20 20"><circle cx="8" cy="8" r="5.5" fill="none" stroke="#2b2b2b" stroke-width="1.6"/><line x1="12" y1="12" x2="17" y2="17" stroke="#2b2b2b" stroke-width="1.6"/></svg>
      <svg class="nav__icon" viewBox="0 0 20 20"><path d="M3 5h14l-2 9H5z" fill="none" stroke="#2b2b2b" stroke-width="1.5"/><circle cx="16" cy="4" r="3" fill="#3277b5"/></svg>
    </nav>
  </div>
  <div class="contact">
    <h2 class="contact__title">CONTACT US</h2>
    <p class="contact__lead">This contact form is a dead mail if you really want to get in touch with us,<br>send an email to support@quiltrest.com</p>
    <div class="contact__form">
      <span class="contact__label">Name</span><div class="contact__field">your name</div>
      <span class="contact__label">Email</span><div class="contact__field">your mail</div>
      <span class="contact__label">Message</span><div class="contact__field contact__field--area">description</div>
      <span class="contact__submit">SUBMIT</span>
    </div>
  </div>
  <div class="newsletter">
    <div class="newsletter__title">SUBSCRIBE TO OUR NEWSLETTER</div>
    <div class="newsletter__form"><div class="newsletter__input">Enter your email address</div><div class="newsletter__btn">SUBSCRIBE</div></div>
  </div>
  <div class="footer">
    <div><div class="footer__heading">MY ACCOUNT</div><div class="footer__link">My Orders</div><div class="footer__link">My Vouchers</div><div class="footer__link">My Address</div><div class="footer__link">My Credit Slip</div><div class="footer__link">My History</div></div>
    <div><div class="footer__heading">INFORMATION</div><div class="footer__link">Contact Us</div><div class="footer__link">Search Terms</div><div class="footer__link">Shipping Guide</div><div class="footer__link">Term Of Use</div><div class="footer__link">Affiliate</div></div>
    <div><div class="footer__heading">EXTRA</div><div class="footer__link">Brand Partners</div><div class="footer__link">Gift Vouchers</div><div class="footer__link">Specials</div><div class="footer__link">Promotions</div><div class="footer__link">Wishlist</div></div>
    <div><div class="footer__heading">COLLECTION</div><div class="footer__link">Decorations</div><div class="footer__link">Living Room</div><div class="footer__link">Specials</div><div class="footer__link">Office Care</div><div class="footer__link">Kitchen Care</div></div>
    <div><div class="footer__heading">FOLLOW US</div><div class="footer__link"><span class="footer__social"></span>Facefolio</div><div class="footer__link"><span class="footer__social"></span>Chirper</div><div class="footer__link"><span class="footer__social"></span>Searchly+</div><div class="footer__link"><span class="footer__social"></span>Linkward</div></div>
  </div>
  <div class="bottombar">
    <span class="bottombar__copy">2017 © Copyright . All rights reserved</span>
    <div class="payments"><span class="payment payment--sky"></span><span class="payment payment--navy"></span><span class="payment"></span><span class="payment"></span><span class="payment payment--blue"></span><span class="payment payment--sky"></span></div>
  </div>
</section>

</body>
</html>
```